the look of import selling star-up company

I have attached rhino logo that i like (can be edit) and i wanna turn that in to luxury look. Example like black base and gold logo +luxury looking font.

Company name: Kestora Imports Oy
Slogan: Finish that lasts.
CEO Juho Kettumaa
Starting to import ceramic nano coatings to cars, in home use and industrial purposes.

Target Market(s)

30-60 year old men and women ho have big money and know what car they drive

Industry/Entity Type

It Company

```html
<!DOCTYPE html>
<html lang="en">
<head>
<meta charset="utf-8">
<title>Kestora Imports Oy — Business Card</title>
<link rel="stylesheet" href="https://fonts.googleapis.com/css2?family=Roboto:wght@400;700&display=swap">
<style>
  :root {
    --backdrop: #8c8c8c;
    --card: #1c1c1c;
    --gold: #d9b233;
    --ink: #ececec;
    --ink-soft: #cfcfcf;
  }
  * { margin: 0; padding: 0; box-sizing: border-box; }
  html, body {
    width: 1200px;
    height: 781px;
    overflow: hidden;
    background: var(--backdrop);
  }
  .canvas {
    position: relative;
    width: 1200px;
    height: 781px;
  }
  .card {
    position: absolute;
    left: 374px;
    width: 452px;
    height: 251px;
    background: var(--card);
    color: var(--ink);
    font-family: "Roboto", Arial, sans-serif;
  }
  .card--front { top: 103px; }
  .card--back  { top: 409px; }

  .brand-disc {
    position: absolute;
    width: 96px;
    height: 96px;
    border-radius: 50%;
    background: var(--gold);
  }
  .brand-name,
  .brand-tagline {
    position: absolute;
    font-family: "Roboto", Arial, sans-serif;
    color: var(--gold);
    white-space: nowrap;
    transform: translateX(-50%);
    line-height: 1;
  }
  .brand-name { font-weight: 700; letter-spacing: 0.02em; }
  .brand-tagline { font-weight: 400; letter-spacing: 0.12em; }

  /* front */
  .card--front .brand-disc { left: 178px; top: 59px; }
  .card--front .brand-name { left: 226px; top: 164px; font-size: 22px; }
  .card--front .brand-tagline { left: 226px; top: 192px; font-size: 10.5px; }

  /* back */
  .card--back .brand-disc { left: 291px; top: 26px; }
  .card--back .brand-name { left: 339px; top: 132px; font-size: 18px; }
  .card--back .brand-tagline { left: 339px; top: 155px; font-size: 8.5px; }

  .person {
    position: absolute;
    left: 19px;
    top: 22px;
  }
  .person__name { font-weight: 700; font-size: 17px; color: var(--ink); }
  .person__role { font-size: 10px; color: var(--ink-soft); margin-top: 2px; }

  .address {
    position: absolute;
    left: 19px;
    top: 157px;
    font-size: 11px;
    line-height: 14px;
    font-style: normal;
    color: var(--ink-soft);
  }
  .contact-list {
    position: absolute;
    left: 19px;
    top: 193px;
    list-style: none;
    font-size: 11px;
    color: var(--ink-soft);
  }
  .contact-list li {
    display: flex;
    align-items: center;
    height: 15px;
  }
  .contact-list svg {
    width: 10px;
    height: 10px;
    margin-right: 13px;
    fill: var(--ink-soft);
  }
</style>
</head>
<body>
<main class="canvas">
  <section class="card card--front" aria-label="Card front">
    <div class="brand-disc"></div>
    <div class="brand-name">KESTORA IMPORTS OY</div>
    <div class="brand-tagline">FINISH THAT LASTS</div>
  </section>

  <section class="card card--back" aria-label="Card back">
    <div class="person">
      <div class="person__name">Juho Kettumaa</div>
      <div class="person__role">CEO</div>
    </div>

    <div class="brand-disc"></div>
    <div class="brand-name">KESTORA IMPORTS OY</div>
    <div class="brand-tagline">FINISH THAT LASTS</div>

    <address class="address">
      48 Harbour Lane<br>
      Eastport City 20410
    </address>

    <ul class="contact-list">
      <li>
        <svg viewBox="0 0 10 10" aria-hidden="true"><path d="M1 2.5c0-1 1-1.5 4-1.5s4 .5 4 1.5v1H7V2.6H3v.9H1zM2 4.5h6l1 4.5H1z"/></svg>
        000-222-3333
      </li>
      <li>
        <svg viewBox="0 0 10 10" aria-hidden="true"><path d="M0 2h10v6H0z M0.8 2.6 5 5.6l4.2-3V2.6L5 5.2z" fill-rule="evenodd"/></svg>
        juho@kestoraimports.com
      </li>
      <li>
        <svg viewBox="0 0 10 10" aria-hidden="true"><path d="M5 0.5a4.5 4.5 0 1 0 0 9a4.5 4.5 0 1 0 0-9zm0 1c.7 0 1.4 1.3 1.5 3H3.5c.1-1.7.8-3 1.5-3zM1.6 4.5h1.1c0-1 .2-1.9.6-2.6a3.5 3.5 0 0 0-1.7 2.6zm5.7 0h1.1a3.5 3.5 0 0 0-1.7-2.6c.4.7.6 1.6.6 2.6zM1.6 5.5a3.5 3.5 0 0 0 1.7 2.6c-.4-.7-.6-1.6-.6-2.6zm1.9 0c.1 1.7.8 3 1.5 3s1.4-1.3 1.5-3zm3.8 0c0 1-.2 1.9-.6 2.6a3.5 3.5 0 0 0 1.7-2.6z"/></svg>
        www.kestoraimports.com
      </li>
    </ul>
  </section>
</main>
</body>
</html>
```